Calder Wynd Company Profile

We have all the written content for our company profile and just need the background graphics and layout designed, this can be seen at our website www.calder-wynd.example or in the attached company profiles
We are happy with the content as far as wording and our logo are concerned, we are looking to revamp the background and layout.
The intention is for this to be printed as a brochure where the inside of the rear page has a pocket at the bottom so that our relevant affiliated companies brochures can be inserted into to complete the package depending on who we are presenting it to.

Target Market(s)

Oil & Gas, Power Generation, Mining, Maritime, Marine, Automation, Engineering

Industry/Entity Type

Engineering Consulting

Colors

Designer to choose colors to be used in the design.

Requirements
Must have
• Existing provided content
Nice to have
• engineering background and images that pop
Should not have
• our target market is Oil & Gas, Power Generation, Mining, Maritime, Marine, Automation, Engineering so it should not have content that does not relate to these industries

```html
<!DOCTYPE html>
<html lang="en">
<head>
<meta charset="utf-8">
<title>Calder Wynd Company Profile</title>
<link href="https://fonts.googleapis.com/css2?family=Teko:wght@400;500&family=Lato:wght@400;700;900&display=swap" rel="stylesheet">
<style>
:root{
  --bg:#c6ad90;
  --panel-light:#ffffff;
  --panel-mid:#e4e4e4;
  --header:#434343;
  --orange:#e8850f;
  --text:#3a3a3a;
  --rule:#bdbdbd;
  --white:#ffffff;
}
*{box-sizing:border-box;margin:0;padding:0}
html,body{width:1200px;height:1200px;overflow:hidden}
body{background:var(--bg);font-family:'Lato',sans-serif;color:var(--text);position:relative}
.sheet{position:absolute;left:221px;width:710px;height:502px;display:flex}
.sheet--outer{top:44px}
.sheet--inner{top:614px}
.panel{position:relative;height:100%;background:linear-gradient(90deg,var(--panel-light) 0%,#f4f4f4 55%,var(--panel-mid) 100%);overflow:hidden}
.panel--a{width:237px}
.panel--b{width:240px}
.panel--c{width:233px}
.photo{position:absolute;left:0;top:0;width:100%}
.sheet--outer .photo{height:300px}
.sheet--inner .photo{height:147px}
.photo--pylons{background:linear-gradient(165deg,#1c3f9c 0%,#3f6fcf 35%,#8a90a8 60%,#d99a4a 82%,#7a5530 100%)}
.photo--conveyor{background:linear-gradient(180deg,#5d7a8a 0%,#3f5a4c 25%,#2f4a32 55%,#9a7a3a 80%,#4a3d2a 100%)}
.photo--plant{background:linear-gradient(160deg,#3a2a6a 0%,#7a3a5a 30%,#b8902a 55%,#7a5a1a 80%,#2a2030 100%)}
.photo--refinery-a{background:linear-gradient(180deg,#6a88b8 0%,#3d5d96 45%,#1f3a66 75%,#12223e 100%)}
.photo--refinery-b{background:linear-gradient(180deg,#7a9ac0 0%,#4a6aa0 45%,#2a4470 75%,#14243e 100%)}
.photo--refinery-c{background:linear-gradient(180deg,#5a6a90 0%,#c8883a 45%,#f0b030 58%,#4a4a5a 80%,#1a2232 100%)}
.head{position:absolute;background:var(--header);color:var(--white);font-family:'Teko',sans-serif;font-weight:400;text-align:center;display:flex;flex-direction:column;justify-content:center;line-height:.95;letter-spacing:.5px}
.head .accent{color:var(--orange)}
.head--row{flex-direction:row;align-items:center;gap:5px}
.sheet--outer .head{left:24px;top:279px;width:189px;height:53px;font-size:23px}
.head--wide{font-size:19px!important;left:19px!important;width:189px!important}
.sheet--inner .head{top:122px;height:53px;font-size:22px;font-weight:500;letter-spacing:1px}
.head--marine{left:24px;width:189px}
.head--hydraulic{left:22px;width:190px}
.head--electronics{left:19px;width:188px;height:44px!important;font-size:15px!important;font-weight:400!important;letter-spacing:0!important}
.body{position:absolute;left:24px;right:22px;font-size:6.4px;line-height:1.35}
.body p{margin-bottom:6px}
.body--tight{line-height:1.28}
.body--tight p{margin-bottom:4px}
.about{top:366px}
.contact{position:absolute;left:48px;width:142px;top:338px}
.contact-row{display:flex;align-items:center;gap:8px;border-bottom:1.5px solid var(--rule);font-size:7.4px;padding:6px 0 8px}
.contact-row svg{flex:none}
.contact-row--tall{align-items:flex-start}
.badges{position:absolute;left:93px;top:440px;display:flex;gap:2px}
.badge{width:24px;height:30px;border:1.5px solid #2a3f8a;background:#fff}
.badge--fill{background:#2a3f8a;border-color:#2a3f8a}
.brand{position:absolute;left:22px;top:390px;display:flex;align-items:center;gap:7px}
.brand-mark{width:26px;height:26px;background:var(--orange)}
.brand-name{font-family:'Lato',sans-serif;font-weight:900;font-size:23px;color:#555;line-height:1}
.lead{font-family:'Teko',sans-serif;color:var(--orange);font-size:11.5px;line-height:.95;margin:6px 0 4px}
.list{list-style:none;margin-bottom:6px}
.body--tight .list{margin-bottom:4px}
.list li{padding-left:6px;position:relative}
.list li::before{content:"";position:absolute;left:0;top:2.6px;width:2.5px;height:2.5px;border-radius:50%;background:var(--orange)}
.team{display:flex;gap:6px;margin-top:8px}
.member{flex:1;border-left:1px solid var(--rule);padding-left:4px;font-size:4px;line-height:1.3;white-space:nowrap;overflow:hidden}
.member:first-child{border-left:0;padding-left:0}
.member strong{display:block;font-family:'Teko',sans-serif;font-weight:400;color:var(--orange);font-size:7.5px;line-height:1}
.sub-head{position:relative;background:var(--header);color:var(--white);font-family:'Teko',sans-serif;font-weight:500;font-size:20px;letter-spacing:1px;text-align:center;line-height:.95;display:flex;flex-direction:column;justify-content:center}
.sub-head .accent{color:var(--orange)}
.sub-head--piping{height:33px;flex-direction:row;align-items:center;gap:6px;margin:9px 0 12px}
.sub-head--cargo{height:50px;margin:5px 0 8px}
.two-col{display:flex;gap:14px}
.lead--center{text-align:center;font-size:12.5px;margin-top:10px}
.screens{display:grid;grid-template-columns:1fr 1fr;gap:2px;margin-top:6px;height:126px}
.screen{background:linear-gradient(180deg,#1e2a44 0%,#33476e 60%,#1a2235 100%)}
.screen--console{background:linear-gradient(180deg,#4a5060 0%,#2a3a5a 50%,#3a3a3a 100%)}
</style>
</head>
<body>

<section class="sheet sheet--outer" aria-label="Outer side of brochure">
  <div class="panel panel--a">
    <div class="photo photo--pylons" role="img" aria-label="Electricity pylons against a blue and orange sunset sky"></div>
    <h2 class="head head--row">ABOUT <span class="accent">US</span></h2>
    <div class="body about">
      <p>Providing technical manpower and consultancy services deployable with minimal notice to any location at any time globally for the maritime, oil and gas, power generation, civil, industrial and mining industries.</p>
      <p>Our team includes multi-lingual, multi-skilled and experienced consultants working in projects in some of the world's most competitive, challenging and bureaucratic locations. We pride ourselves on having the capability to mobilize highly skills individuals into harsh and challenging environments.</p>
    </div>
  </div>

  <div class="panel panel--b">
    <div class="photo photo--conveyor" role="img" aria-label="Mining conveyor structure in front of forested mountains"></div>
    <h2 class="head head--row">CONTACT <span class="accent">US</span></h2>
    <div class="contact">
      <div class="contact-row">
        <svg width="12" height="12" viewBox="0 0 24 24"><path fill="#e8850f" d="M6.6 10.8a15 15 0 0 0 6.6 6.6l2.2-2.2a1 1 0 0 1 1-.25 11.4 11.4 0 0 0 3.6.57 1 1 0 0 1 1 1V20a1 1 0 0 1-1 1A17 17 0 0 1 3 4a1 1 0 0 1 1-1h3.5a1 1 0 0 1 1 1c0 1.25.2 2.450.57 3.57a1 1 0 0 1-.25 1z"/></svg>
        <span>+44-1632-960-418</span>
      </div>
      <div class="contact-row">
        <svg width="13" height="10" viewBox="0 0 26 20"><rect x="1" y="1" width="24" height="18" fill="none" stroke="#e8850f" stroke-width="2.4"/><path d="M1 1l12 10L25 1" fill="none" stroke="#e8850f" stroke-width="2.4"/></svg>
        <span>consultants@calder-wynd.example</span>
      </div>
      <div class="contact-row contact-row--tall">
        <svg width="11" height="15" viewBox="0 0 22 30"><path fill="#e8850f" d="M11 0a11 11 0 0 0-11 11c0 8 11 19 11 19s11-11 11-19A11 11 0 0 0 11 0zm0 15a4 4 0 1 1 0-8 4 4 0 0 1 0 8z"/></svg>
        <span>Harbour Point, 12 Quay Road,<br>Central Docks</span>
      </div>
    </div>
    <div class="badges" aria-label="Certification badges">
      <div class="badge"></div>
      <div class="badge badge--fill"></div>
    </div>
  </div>

  <div class="panel panel--c">
    <div class="photo photo--plant" role="img" aria-label="Illuminated power plant with chimney and workers at night"></div>
    <h2 class="head head--wide">TECHNICAL MANPOWER<span class="accent">&amp; CONSULTANCY SERVICES</span></h2>
    <div class="brand">
      <span class="brand-mark"></span>
      <span class="brand-name">CALDER WYND</span>
    </div>
  </div>
</section>

<section class="sheet sheet--inner" aria-label="Inner side of brochure">
  <div class="panel panel--a">
    <div class="photo photo--refinery-a" role="img" aria-label="Refinery towers under a blue sky"></div>
    <h2 class="head head--marine head--row">Marine <span class="accent">Services</span></h2>
    <div class="body" style="top:182px">
      <p>Calder Wynd Associates Limited (CWAL) specialize in consultancy services, manpower services and technical services for maritime, offshore oil &amp; gas, power generation, mining, refiners and industrial plants world-wide</p>
      <div class="lead">Calder Wynd Marine division, offer services for:</div>
      <ul class="list">
        <li>Marine Hydraulic Systems</li>
        <li>Marine Cargo Pumping Systems</li>
        <li>Marine Hydraulic and Cargo Piping Systems</li>
        <li>Marine Electronics, Control &amp; Alarm Systems, Navigation Bridge Systems</li>
      </ul>
      <p>For further information, ref. to the services information on the following pages</p>
      <div class="team">
        <div class="member"><strong>OWEN PRYCE</strong>Managing Director<br>opryce@calder-wynd.example<br>+44 1632 960 101</div>
        <div class="member"><strong>LARS VEITEN</strong>Technical Director<br>lveiten@calder-wynd.example<br>+44 1632 960 202</div>
        <div class="member"><strong>TORE BRANNVIK</strong>Projects Manager<br>tbrannvik@calder-wynd.example<br>+44 1632 960 303</div>
      </div>
      <h3 class="sub-head sub-head--piping">Piping Systems <span class="accent">Services</span></h3>
      <p>Hydraulic, Cargo, Control, Instrument, welded, weld free and multicore Pipe systems.</p>
      <ul class="list">
        <li>Ship Inspection, Pipe systems Inspection, System Engineering.</li>
        <li>Pipe fabrication.</li>
        <li>Testing, pre docking assessments and for purchase of ships.</li>
        <li>Site supervision for hydraulic pipe fabrication, chemical cleaning, installation, oil filling and flushing.</li>
      </ul>
    </div>
  </div>

  <div class="panel panel--b">
    <div class="photo photo--refinery-b" role="img" aria-label="Industrial plant with flare stacks at dusk"></div>
    <h2 class="head head--hydraulic">Hydraulic System<span class="accent">Services</span></h2>
    <div class="body body--tight" style="top:180px;left:22px;right:20px">
      <p style="margin-bottom:2px">Hydraulic System Inspection, testing for pre docking assessments and purchase of ships.</p>
      <div class="lead">CWAL service and provide parts for a wide range of marine hydraulic systems</div>
      <ul class="list">
        <li>Hydraulic Systems and Component Services</li>
        <li>Hydraulic Transmission Systems</li>
        <li>Hydraulic Valve Control Systems</li>
        <li>Steering gear, Cranes, Winches</li>
        <li>Actuators, Cylinders, Pumps and Motor repairs</li>
      </ul>
      <div class="lead">We provide:</div>
      <div class="two-col">
        <ul class="list"><li>Hydraulic System Engineering</li><li>Hydraulic Service Engineers</li></ul>
        <ul class="list"><li>Supervisors</li></ul>
      </div>
      <h3 class="sub-head sub-head--cargo">Cargo Pumping Systems<span class="accent">Services</span></h3>
      <p>CWAL service the most common pump types Chemical, Product, Oil and LPG tankers, Submerged and Conventional Pump room systems. Aldren - Fjordvik - Kestrel - Norhaven - Vantor and others</p>
      <ul class="list">
        <li>Submerged hydraulically driven pumps and "long shaft" pumps for Chemical Product and LPG ships.</li>
        <li>Pump room installed pumping systems</li>
        <li>Reconditioning of pump housings, shafts and impellers, repair leaking (cracked, pitted or corroded pipe-stacks) and also supervise such work at sites and shipyards, worldwide.</li>
        <li>Emergency repair of pumps, pipe stack and pump housings by use of composite materials.</li>
        <li>Pump system Inspection, testing for pre-docking assessments and change of owners/management</li>
      </ul>
    </div>
  </div>

  <div class="panel panel--c">
    <div class="photo photo--refinery-c" role="img" aria-label="Refinery silhouette against an orange sunset"></div>
    <h2 class="head head--electronics">Marine Electronics, Controls and Alarm<span class="accent">Systems</span></h2>
    <div class="body" style="top:176px;left:19px;right:25px">
      <p style="margin-bottom:2px">CWAL offer full range technical services for Marine Control &amp; Alarm Systems</p>
      <div class="lead">Project Engineering, HW / SW for New Installations, Upgrade and Retrofits</div>
      <ul class="list">
        <li>System's Troubleshooting, Repairs and upgrades.</li>
        <li>Upgrade of outdated controls and alarm systems</li>
        <li>Navigation bridge system services.</li>
        <li>Control &amp; Alarm System Inspection, testing for pre-docking assessments and change of Owners / Management</li>
      </ul>
      <div class="lead">Other Products and Services</div>
      <p>Boiler Control system Refit.<br>Valve Control modules.<br>Navigation Light controller E0 Call system</p>
      <div class="lead lead--center">Recently installed Engine Alarm and Cargo control &amp; alarm systems</div>
      <div class="screens">
        <div class="screen" role="img" aria-label="Engine alarm monitoring screen"></div>
        <div class="screen" role="img" aria-label="Cargo control system screen"></div>
        <div class="screen" role="img" aria-label="Alarm system overview screen"></div>
        <div class="screen" role="img" aria-label="Control panel display"></div>
        <div class="screen screen--console" role="img" aria-label="Control room console"></div>
        <div class="screen screen--console" role="img" aria-label="Bridge control desk"></div>
      </div>
    </div>
  </div>
</section>

</body>
</html>
```